Website that informs user about the Darknet

A short 1 pager website that explains what the darknet is.
Current site: https://velmora.gs/ & https://quintaro.kr/. No logo needed. Just an informational page. Choose the layout / colours that you prefer.

Target Market(s)

Endusers, companies etc.

Coding

Coded - Design and coding required

Number of Pages Required

1 page

Requirements
Must have
• 1 Small contact form - thats all
Should not have
• The page must look professional. Not for kids. I target mainly adults / employees

```html
<!DOCTYPE html>
<html lang="en">
<head>
<meta charset="utf-8">
<title>Veltrix - Cyber Threat Intelligence - Darknet and Dark Web</title>
<link href="https://fonts.googleapis.com/css2?family=Arimo:ital,wght@0,400;0,700;1,400;1,700&display=swap" rel="stylesheet">
<style>
:root{
  --black:#000;
  --ink:#222;
  --text:#333;
  --white:#fff;
  --gold:#f2b51b;
  --card:#1e1e1e;
  --link:#1a5fd0;
  --orange:#f68b2c;
  --line:#c9c9c9;
}
*{box-sizing:border-box;margin:0;padding:0}
html,body{width:1200px;height:2673px;overflow:hidden}
body{font-family:"Arimo",Arial,sans-serif;background:var(--white);color:var(--text);position:relative}
a{color:var(--link)}
.site-header{position:absolute;left:0;top:0;width:1200px;height:175px;background:var(--black)}
.header-photo{position:absolute;left:0;top:0;width:264px;height:175px;background:linear-gradient(135deg,#0c2b3c,#0a4a6a 55%,#03121c)}
.brand{position:absolute;left:380px;top:38px;width:300px;color:var(--gold);font-style:italic;font-weight:700;font-size:18px;line-height:38px}
.nav{position:absolute;left:718px;top:74px;display:flex;gap:43px}
.nav a{color:var(--white);font-weight:700;font-size:19px;text-decoration:none}
.page-title{position:absolute;left:369px;top:200px;width:463px;text-align:center;font-size:34px;font-weight:700;color:var(--ink);padding-bottom:4px;border-bottom:2px solid var(--ink)}
.intro-col{position:absolute;top:272px;width:325px}
.intro-col h2{font-size:28px;font-weight:700;color:var(--ink);text-align:center;line-height:32px;margin-bottom:24px}
.intro-col p{font-size:12px;font-style:italic;line-height:17.6px;text-align:justify;color:var(--text)}
.col-a{left:60px}.col-b{left:438px}.col-c{left:817px}
.onion-link{display:block;margin:22px 0 0 11px;font-size:12px;font-style:italic;line-height:17.6px;word-break:break-all}
.binary-art{width:325px;height:198px;margin-top:10px;background:linear-gradient(180deg,#6d6d6d,#9a9a9a 50%,#5a5a5a)}
.hero-photo{position:absolute;left:0;top:830px;width:1200px;height:572px;background:radial-gradient(ellipse at 50% 45%,#1a1a1a 0,#05060f 35%,#0a1030 70%,#0b1a5a 100%)}
.monitor-band{position:absolute;left:0;top:1402px;width:1200px;height:230px;background:var(--black);color:var(--white);text-align:center}
.monitor-band h2{display:inline-block;margin-top:24px;font-size:32px;font-weight:700;padding:0 24px 6px;border-bottom:2px solid var(--white)}
.monitor-band p{width:1080px;margin:12px auto 0;font-size:12px;font-weight:700;line-height:17.6px;color:var(--white)}
.topic{position:absolute;width:521px}
.topic h3{height:91px;background:var(--card);color:var(--white);font-size:28px;font-weight:700;text-align:center;line-height:31px;padding-top:14px}
.topic p,.topic ul{margin-top:25px;font-size:12px;font-style:italic;line-height:17.6px;text-align:justify;color:var(--text)}
.topic ul{padding-left:36px;text-align:left}
.t1{left:60px;top:1665px}.t2{left:620px;top:1665px}.t3{left:60px;top:1963px}.t4{left:620px;top:1963px}
.contact-band{position:absolute;left:0;top:2255px;width:1200px;height:65px;background:var(--black);color:var(--white);text-align:center;font-size:32px;font-weight:700;line-height:65px}
.contact-form{position:absolute;left:60px;top:2340px;width:1081px}
.contact-form label{display:block;font-size:16px;font-style:italic;font-weight:700;color:var(--ink);margin-bottom:6px}
.contact-form .field{display:block;width:1081px;height:33px;border:1px solid var(--line);margin-bottom:14px;font-family:inherit}
.contact-form textarea.field{height:51px;padding:10px;font-size:12px;color:#888;resize:vertical}
.send{width:65px;height:34px;background:var(--orange);color:var(--white);border:none;font-family:inherit;font-style:italic;font-weight:700;font-size:16px}
.site-footer{position:absolute;left:0;top:2613px;width:1200px;height:60px;background:var(--black);color:var(--white);text-align:center;font-weight:700;font-size:16px;line-height:22px;padding-top:8px}
.site-footer em{display:block}
</style>
</head>
<body>
<header class="site-header">
  <div class="header-photo" role="img" aria-label="Hooded figure typing on a laptop surrounded by blue code"></div>
  <div class="brand">VELTRIX - CYBER THREAT INTELLIGENCE - DARKNET AND DARK WEB</div>
  <nav class="nav"><a href="#">Start</a><a href="#contact">Contact us</a></nav>
</header>

<h1 class="page-title">DARKNET AND DARK WEB</h1>

<section class="intro-col col-a">
  <h2>What is the internet?</h2>
  <p>The Internet is a network of computers that are connected to each other through a global network. Instead of computers, in this context we also speak of servers, such as web servers. If someone sets up a web server with a website on the Internet, this website can be accessed by all computers or mobile devices connected to the Internet. To do this, one uses a web browser such as Orbit, Nimbus or many others. The websites are usually configured under domains, which the user must remember. For example, one domain is <a href="#">www.brightseek.com.</a> When you enter a domain in the web browser, your computer will look for the server where the website is located. The location of the server is indicated by an IP address. You can think of the IP address as a house number that uniquely specifies the location of the server. For example, the IP address of Brightseek is 198.51.100.24. Access to the web pages can be unencrypted (displayed in the web browser with <a href="#">http://domain.com)</a> or encrypted (displayed in the web browser with <a href="#">https://domain.com).</a> Because these web pages are visible to everyone, search engines like Brightseek or Findora can also find and index them. If you want to find out who is operating a website, you can query this by means of WHOIS information at the respective domain provider, provided that the owner has given the release of the registration information. Here is an example of such a WHOIS query form, which can be accessed by anyone on the Internet: <a href="#">https://whois.lookupdesk.com/</a></p>
</section>

<section class="intro-col col-b">
  <h2>So how is the internet different to the darknet?</h2>
  <p>TheDarknet is similar to the Internet, but there are significant differences.Similar to the Internet, the Darknet is only a network of computers (servers)that are connected to each other. Unlike the Internet, however, you can'taccess the websites with a regular web browser, for example, but with specialsoftware like the Onyx Browser. This browser can be installed as an app on thePC or mobile device and access to the darknet is achieved within a few minutes.The special thing about software like the Onyx Browser, however, is thatcommunication to the server runs completely encrypted over many other PCs.Everything is encrypted - even the IP address of the systems you arecommunicating with. Because the connection runs over many PCs, you don't known which server the website you are accessing is located. Therefore, websitescan be operated completely anonymously. In contrast to domains on the Internet,the websites also use much more cryptic names. For example, a darknet domain does notend in .com or similar, but in .onion. Here is an example of a darknet domain(search engine) that can be accessed in the Onyx browser:</p>
  <a class="onion-link" href="#">http://qorvantelxp42mkd81trayzeplk5vmnwaqu3ebxh7sandfitcro9lyd.onion/</a>
</section>

<section class="intro-col col-c">
  <h2>Is the darknet illigal?</h2>
  <p>Many think the darknet and access is criminell. But this is not the case. The idea of the darknet comes from the desire to create anonymity. Therefore, the darknet makes sense for the exchange of protected business information or communication of political activists. Unfortunately, only criminal elements also seek anonymity. For example, anyone can upload a website completely anonymously to sell drugs or stolen business data. Thanks to anonymous means of payment such as Nodecoin, such business processes can also run smoothly. &nbsp;Both the dark web and the deep web cannot be found in search engine results, or only with great difficulty.</p>
  <div class="binary-art" role="img" aria-label="Grey eye shape made of binary digits"></div>
</section>

<div class="hero-photo" role="img" aria-label="Hooded figure in shadow against blue digital data streams"></div>

<section class="monitor-band">
  <h2>WHY AND HOW CAN THE DARKNET BE MONITORED?</h2>
  <p>The dark web can be a scary place. Especially if you're new to it and are not properly equipped with all you need to scour safely.<br>Dark web monitoring refers to the process by which you can search, track, or monitor the information regarding your organization on the dark web. With the right tools on the dark web, you can track lost, stolen, or leaked information such as intellectual property, compromised passwords, breached credentials, leaked organization's sensitive data, etc. Oftentimes, these sensitive information are usually transacted among unscrupulous characters in the dark web. &nbsp;With proper dark web monitoring tools, you can better detect threats and dangers on the dark web, which is a step further than just anti-virus, anti-malware programs, and programs that help in identity theft monitoring. In the case of these anti-malware and antivirus programs, they help you monitor and prevent any malicious code aimed at stealing information. However, they do very little in situations, where the deed has already been done.</p>
</section>

<section class="topic t1">
  <h3>How does dark web<br>monitoring work?</h3>
  <p>When you utilize these dark web monitoring tools, there is a constant search for stolen, lost, or leaked information in the dark web, in real time. Millions of sites all over the dark are searched simultaneously for specific information like email addresses of the corporation, or general information like the name of the company or industry you operate in. &nbsp;When any impending threat or loss of information is found, you will receive an alert which can be customized by you. This alert notifies just about anyone or any team relevant to the threat like the legal, marketing, fraud teams, or even human resources.</p>
</section>

<section class="topic t2">
  <h3>Features found<br>in dark web monitoring</h3>
  <ul>
    <li>Threat intelligence When the darknet monitoring service receives data matching the search terms, this data is automatically forwarded to the CISO or a SOC (Security Operations Center).</li>
    <li>Threat hunting For individuals who are considered threat hunters, monitoring the dark web can help speed up their search and give them a more complete picture of the danger and nature of a potential threat. This can help prevent phishing or ransomware attacks, for example.</li>
    <li>Quicker incidence response &nbsp;With quicker responses to incidences of threat and danger, there will be faster threat mitigation.</li>
  </ul>
</section>

<section class="topic t3">
  <h3>Why should you use<br>dark web monitoring?</h3>
  <p>On the dark web, there are a lot of things to worry about. Apart from lost credentials, dark web monitoring can also reveal chatter or activity around a business or company that has been attacked, is under attack, or reveal any impending attack. &nbsp;Using this service, you can classify or rank risks from unknown sources in order of severity, and businesses can use this classification to identify and mitigate dangers quicker. Some of those risks include;&bull; Data dumps to criminal chatrooms or hackers forum &bull; Third party breaches&bull; P2P leaks &bull; Brand misuse &bull; Accidental leaks &nbsp;&bull; Domain spoofing &bull; Impersonations &bull; Potential threats</p>
</section>

<section class="topic t4">
  <h3>Benefits<br>of dark web monitoring</h3>
  <p>Dark web monitoring affords you with the ability to track leaked data and the time it has spent released. Actively monitoring the dark web with these tools, give cybercriminals less time to execute attacks and leak sensitive information. &nbsp;Additionally, businesses that monitor the dark web can find out if a breach is imminent, or if they are likely to be breached. If a breach does happen, it will give them an insight as to who is leading the attack and what method of attack is being employed. &nbsp;&nbsp;Who needs dark web monitoring tools? Simply put, everybody. These services are important to businesses or individuals whose job is to protect the online presence of other businesses. It is also for businesses with valuable intellectual or sensitive information that may be a target to cybercriminals.</p>
</section>

<div class="contact-band" id="contact">Contact us</div>

<form class="contact-form">
  <label for="name">Name</label>
  <input class="field" id="name" type="text">
  <label for="email">Email Address</label>
  <input class="field" id="email" type="email">
  <textarea class="field" placeholder="Message"></textarea>
  <button class="send" type="button">Send</button>
</form>

<footer class="site-footer">
  Copyright &copy; 2022 Veltrix - Cyber Threat Intelligence - Darknet and dark web - All Rights Reserved.
  <em>Not powered by the Darknet</em>
</footer>
</body>
</html>
```